We sell companies excess stock for them

We need a business card for a company based in New Zealand called 'StockHarbor'.

Check out our website to get an idea www.stockharbor.example

We help other businesses to;
- Sell Excess Stock
- Manage Product Returns
- Sell Company Assets

Our logo is attached for your reference
The font used is 'RifficFree-Bold'

Target Market(s)

Businesses

Industry/Entity Type

Business

Contact Information for Business Card

Name: Mark Pellow
Phone: 027 846 2093
email: markpellow@stockharbor.example
website: www.stockharbor.example

Font styles to use
Other font styles liked:
• Unsure

Colors
9bcb3b

Requirements
Must have
• coming soon
Nice to have
• coming soon
Should not have
• coming soon

```html
<!DOCTYPE html>
<html lang="en">
<head>
<meta charset="utf-8">
<title>StockHarbor Business Card</title>
<link rel="stylesheet" href="https://fonts.googleapis.com/css2?family=Fredoka:wght@600&family=Roboto:wght@400;500;700&display=swap">
<style>
  :root {
    --stage: #2b2b2b;
    --paper: #f2f2f2;
    --brand-green: #9bbb10;
    --ink: #333130;
    --ink-soft: #4a4a4a;
    --white: #ffffff;
    --rule: #555555;
  }
  * { margin: 0; padding: 0; box-sizing: border-box; }
  html, body { width: 1200px; height: 960px; overflow: hidden; background: var(--stage); }
  .canvas { position: relative; width: 1200px; height: 960px; }

  .card {
    position: absolute;
    width: 600px;
    height: 343px;
    border-radius: 22px;
  }
  .card-front { left: 314px; top: 113px; background: var(--paper); }
  .card-back { left: 311px; top: 472px; background: var(--brand-green); }

  .brand-mark {
    position: absolute;
    left: 104px; top: 40px;
    width: 44px; height: 44px;
    border-radius: 50%;
    background: var(--brand-green);
  }
  .wordmark {
    position: absolute;
    font-family: 'Fredoka', sans-serif;
    font-weight: 600;
    letter-spacing: -0.5px;
    white-space: nowrap;
  }
  .card-front .wordmark {
    left: 42px; top: 126px;
    font-size: 40px; line-height: 48px;
    color: var(--ink);
  }
  .holder-name {
    position: absolute;
    right: 43px; top: 201px;
    font-family: 'Fredoka', sans-serif;
    font-weight: 600;
    font-size: 21px; line-height: 28px;
    letter-spacing: 0.5px;
    color: var(--ink);
  }
  .holder-name .surname { color: var(--brand-green); }
  .name-rule {
    position: absolute;
    left: 43px; right: 44px; top: 236px;
    height: 1px; background: var(--rule);
  }
  .edge-tab {
    position: absolute;
    right: 0; top: 198px;
    width: 8px; height: 36px;
    border-radius: 6px 0 0 6px;
    background: var(--brand-green);
  }
  .contact-list {
    position: absolute;
    left: 43px; top: 248px;
    list-style: none;
    font-family: 'Roboto', sans-serif;
    font-size: 15px; line-height: 19px;
    color: var(--ink-soft);
  }
  .contact-list li { display: flex; align-items: center; gap: 8px; }
  .contact-list svg { width: 14px; height: 14px; flex: none; fill: var(--brand-green); }

  .card-back .wordmark {
    left: 0; right: 0; top: 132px;
    text-align: center;
    font-size: 52px; line-height: 60px;
    color: var(--white);
  }
  .tagline {
    position: absolute;
    left: 0; right: 0; top: 266px;
    display: flex; justify-content: center; align-items: center; gap: 4px;
    font-family: 'Roboto', sans-serif;
    font-weight: 700;
    font-size: 17px; line-height: 22px;
    color: var(--white);
  }
  .tagline::before, .tagline::after {
    content: ""; width: 80px; height: 1px;
  }
  .tagline::before { background: linear-gradient(to right, rgba(255,255,255,0), #fff); }
  .tagline::after { background: linear-gradient(to left, rgba(255,255,255,0), #fff); }
  .services {
    position: absolute;
    left: 0; right: 0; top: 293px;
    text-align: center;
    font-family: 'Roboto', sans-serif;
    font-size: 14.5px; line-height: 19px;
    color: var(--white);
  }
  .services .dot { padding: 0 3px; }
</style>
</head>
<body>
<main class="canvas">
  <section class="card card-front" aria-label="Card front">
    <div class="brand-mark"></div>
    <div class="wordmark">StockHarbor</div>
    <div class="holder-name">MARK<span class="surname">PELLOW</span></div>
    <div class="name-rule"></div>
    <div class="edge-tab"></div>
    <ul class="contact-list">
      <li>
        <svg viewBox="0 0 16 16" aria-hidden="true"><path d="M3.5 1.5l2.5 0 1 3.5-1.8 1.2a9 9 0 0 0 4.6 4.6l1.2-1.8 3.5 1v2.5c0 .8-.7 1.5-1.5 1.5A12.5 12.5 0 0 1 2 3c0-.8.7-1.5 1.5-1.5z"/></svg>
        027 846 2093
      </li>
      <li>
        <svg viewBox="0 0 16 16" aria-hidden="true"><path d="M1 3.5h14v1.2L8 9 1 4.7z"/><path d="M1 6.2l7 4.3 7-4.3V13H1z"/></svg>
        markpellow@stockharbor.example
      </li>
      <li>
        <svg viewBox="0 0 16 16" aria-hidden="true"><circle cx="8" cy="8" r="7"/><path d="M4 5.5c1.5 0 2 1 3 1.5s.5 2 1.5 2.5-.5 2.5-1.5 3c-.5-1.5-2-2-2.5-3.5S4 7 4 5.5zM9.5 3c1 .5 2.5 0 3 1.5s-1 1.5-2 1.5-1.5-2-1-3z" fill="#f2f2f2"/></svg>
        www.stockharbor.example
      </li>
    </ul>
  </section>

  <section class="card card-back" aria-label="Card back">
    <div class="wordmark">StockHarbor</div>
    <div class="tagline">WE HELP OTHER BUSINESSES TO</div>
    <p class="services">Sell Excess Stock <span class="dot">●</span> Manage Product Returns <span class="dot">●</span> Sell Company Assets</p>
  </section>
</main>
</body>
</html>
```